Zielgruppe
Tobias Fink Personal Training.
Personaltraining für Bürotätige / leitende Positionen.
Rücken- und Haltungstraining.
Zielgruppe: Herren mittleren Alters, gehobene Klasse.
Aufgabenstellung
Schlicht, elegant, hochwertig
Gerne Logo eingearbeitet.
Schwarz / Gold / Weiß

```html
<!DOCTYPE html>
<html lang="de">
<head>
<meta charset="utf-8">
<title>TFPT Visitenkarte</title>
<link href="https://fonts.googleapis.com/css2?family=Open+Sans:wght@400;600&display=swap" rel="stylesheet">
<style>
  :root {
    --stage: #c9c8c9;
    --paper: #ffffff;
    --charcoal: #333333;
    --gold: #c49a2a;
    --ink: #555555;
  }
  * { margin: 0; padding: 0; box-sizing: border-box; }
  html, body { width: 1200px; height: 900px; overflow: hidden; }
  body {
    background: var(--stage);
    font-family: "Open Sans", Arial, sans-serif;
    position: relative;
  }
  .card {
    position: absolute;
    top: 291px;
    width: 540px;
    height: 318px;
    overflow: hidden;
    box-shadow: 0 6px 18px rgba(0,0,0,0.25);
  }
  .card--front { left: 40px; background: var(--paper); }
  .card--back { left: 620px; background: var(--charcoal); }

  /* front */
  .front__tab { position: absolute; left: 0; top: 22px; width: 32px; height: 20px; background: var(--charcoal); }
  .front__brand {
    position: absolute; left: 40px; top: 18px;
    display: flex; align-items: center; gap: 6px;
    font-size: 11px; font-weight: 600; color: var(--gold); line-height: 1;
  }
  .front__brand-mark { width: 8px; height: 8px; background: var(--gold); flex: none; }
  .front__band {
    position: absolute; left: 160px; right: 0; top: 40px; height: 24px;
    background: var(--charcoal); color: var(--paper);
    font-size: 11px; line-height: 24px; text-align: right; padding-right: 44px;
  }
  .front__band-rule { position: absolute; left: 160px; right: 0; top: 68px; height: 1.5px; background: var(--gold); }
  .front__person { position: absolute; left: 40px; top: 100px; color: var(--ink); }
  .front__name { font-size: 14px; }
  .front__role { font-size: 11px; }
  .front__address { position: absolute; left: 40px; top: 160px; color: var(--ink); font-size: 13px; line-height: 19px; font-style: normal; }
  .front__divider { position: absolute; left: 230px; width: 260px; top: 150px; height: 1.5px; background: #222; }
  .front__contacts { position: absolute; left: 300px; top: 222px; list-style: none; color: var(--ink); font-size: 15px; line-height: 22px; }
  .front__contacts li { display: flex; align-items: center; gap: 8px; }
  .front__contacts svg { width: 13px; height: 13px; fill: var(--gold); flex: none; }

  /* back */
  .back__rule { position: absolute; height: 2px; background: var(--gold); }
  .back__rule--left { left: 0; width: 150px; top: 118px; }
  .back__rule--right { right: 0; width: 160px; top: 212px; }
  .back__brand {
    position: absolute; left: 170px; top: 150px;
    display: flex; align-items: center; gap: 10px;
    font-size: 22px; font-weight: 600; color: var(--gold); line-height: 1;
    white-space: nowrap;
  }
  .back__brand-mark { width: 14px; height: 14px; background: var(--gold); flex: none; }
</style>
</head>
<body>
  <section class="card card--front">
    <div class="front__tab"></div>
    <div class="front__brand">
      <span class="front__brand-mark"></span>
      <span>Tobias Fink Personal Training</span>
    </div>
    <div class="front__band">www.tfpt-studio.de</div>
    <div class="front__band-rule"></div>
    <div class="front__person">
      <p class="front__name">Jonas Beispiel</p>
      <p class="front__role">Geschäftsführer</p>
    </div>
    <address class="front__address">
      TFPT Ltd<br>Lindenweg 27<br>A-4150 Birkenau
    </address>
    <div class="front__divider"></div>
    <ul class="front__contacts">
      <li><svg viewBox="0 0 24 24"><path d="M6.6 10.8a15 15 0 0 0 6.6 6.6l2.2-2.2a1 1 0 0 1 1-.25 11.4 11.4 0 0 0 3.6.6 1 1 0 0 1 1 1V20a1 1 0 0 1-1 1A17 17 0 0 1 3 4a1 1 0 0 1 1-1h3.5a1 1 0 0 1 1 1 11.4 11.4 0 0 0 .6 3.6 1 1 0 0 1-.25 1z"/></svg>04711/238 45-10</li>
      <li><svg viewBox="0 0 24 24"><path d="M6 2h10v6H6zM3 9h18v10h-3v3H6v-3H3zm5 7v4h8v-4z"/></svg>04711/238 45-11</li>
      <li><svg viewBox="0 0 24 24"><path d="M2 5h20v14H2zm2 2v.5l8 5.5 8-5.5V7l-8 5.5z"/></svg>info@tfpt-studio.de</li>
    </ul>
  </section>

  <section class="card card--back">
    <div class="back__rule back__rule--left"></div>
    <div class="back__brand">
      <span class="back__brand-mark"></span>
      <span>Tobias Fink Personal Training</span>
    </div>
    <div class="back__rule back__rule--right"></div>
  </section>
</body>
</html>
```